Whispers of Forgotten Ages - belief and superstition in the past

We need a design for a poster for an upcoming exhibition. The exhibition is called " Whispers of Forgotten Ages - an archaeological exhibition about belief and superstition". Doors will be a key concept in the exhibition, a gateway you have to pass to get to the next room. There are seven rooms with different archaeological objects and stories covering the prehistoric and historic times in Northern Zealand.
The seven rooms has the following titles:
Iconography
Amulets/miniatures
Gold room with objects made of gold
Graves
Fire
Offerings
Christianity
The objects on display are mainly from excavations.
The poster must be in an editable format, as the title has to be in danish.
Target Market(s)
Visitors at museums
Industry/Entity Type
Museum
Requirements
Must have
- A door on the poster,somehow
Nice to have
- Something signalling superstition and belief

```html
<!DOCTYPE html>
<html lang="en">
<head>
<meta charset="utf-8">
<title>Whispers of Forgotten Ages – Exhibition Poster</title>
<link href="https://fonts.googleapis.com/css2?family=Lato:wght@400;700&family=Rubik+Distressed&display=swap" rel="stylesheet">
<style>
  :root {
    --red-deep: #8e1420;
    --red: #bd1e30;
    --red-box: rgba(196, 32, 52, 0.9);
    --title: #eadcd5;
    --gold: #f3b46a;
    --white: #ffffff;
  }
  * { margin: 0; padding: 0; box-sizing: border-box; }
  html, body { width: 800px; height: 1200px; overflow: hidden; background: #000; }
  .poster {
    position: relative;
    width: 800px;
    height: 1200px;
    overflow: hidden;
    font-family: "Lato", sans-serif;
  }
  .header-band {
    position: absolute; left: 0; top: 0; width: 800px; height: 118px;
    background: linear-gradient(90deg, var(--red-deep), var(--red));
  }
  .brand {
    position: absolute; left: 436px; top: 44px;
    display: flex; align-items: center; gap: 10px;
    color: var(--white); font-weight: 700;
  }
  .brand-mark { width: 46px; height: 46px; border: 3px solid var(--white); border-radius: 4px; }
  .brand-name { font-size: 20px; line-height: 23px; letter-spacing: 0.5px; }
  .scene-photo { position: absolute; left: 0; top: 118px; width: 800px; height: 1082px; display: block; }
  .block { position: absolute; background: var(--red-box); }
  .block--title { left: 549px; top: 241px; width: 148px; height: 117px; background: rgba(190, 40, 60, 0.55); }
  .block--date { left: 352px; top: 387px; width: 147px; height: 116px; }
  .block--side { left: 0; top: 521px; width: 138px; height: 116px; }
  .block--lower { left: 226px; top: 666px; width: 147px; height: 116px; }
  .block--tagline { left: 377px; top: 925px; width: 423px; height: 117px;
    background: linear-gradient(90deg, #8d1521, var(--red)); }
  .date {
    position: absolute; left: 365px; top: 421px;
    color: var(--gold); font-size: 21px; line-height: 25px;
  }
  .title-line {
    position: absolute; right: 100px;
    font-family: "Rubik Distressed", system-ui, sans-serif;
    font-weight: 400;
    color: var(--title); font-size: 82px; line-height: 1;
    text-transform: uppercase; white-space: nowrap;
  }
  .title-line--1 { top: 250px; }
  .title-line--2 { top: 398px; }
  .title-line--3 { top: 532px; right: 92px; }
  .title-line--4 { top: 676px; right: 92px; }
  .tagline {
    position: absolute; left: 397px; top: 954px;
    color: var(--gold); font-size: 20.5px; line-height: 25px;
  }
  .details {
    position: absolute; left: 397px; top: 1068px; width: 258px;
    color: var(--gold); font-size: 7.8px; line-height: 10px;
  }
</style>
</head>
<body>
<main class="poster">
  <svg class="scene-photo" viewBox="0 0 800 1082" role="img" aria-label="Photograph of tall dark red wooden door frames standing in drifting smoke, with warm orange light spilling across the floor">
    <defs>
      <linearGradient id="frames" x1="0" y1="0" x2="1" y2="0">
        <stop offset="0" stop-color="#2a0b0c"/>
        <stop offset="0.15" stop-color="#7a1418"/>
        <stop offset="0.3" stop-color="#241c1d"/>
        <stop offset="0.45" stop-color="#8a1a1c"/>
        <stop offset="0.6" stop-color="#2b2426"/>
        <stop offset="0.78" stop-color="#5a1214"/>
        <stop offset="0.87" stop-color="#b02226"/>
        <stop offset="0.872" stop-color="#000"/>
        <stop offset="1" stop-color="#000"/>
      </linearGradient>
      <linearGradient id="floor" x1="0" y1="0" x2="0" y2="1">
        <stop offset="0" stop-color="#3a3436" stop-opacity="0.35"/>
        <stop offset="0.55" stop-color="#1a0c0c" stop-opacity="0.2"/>
        <stop offset="0.78" stop-color="#c2361a" stop-opacity="0.55"/>
        <stop offset="1" stop-color="#5a0d0a" stop-opacity="0.9"/>
      </linearGradient>
    </defs>
    <rect width="800" height="1082" fill="url(#frames)"/>
    <rect width="800" height="1082" fill="url(#floor)"/>
  </svg>

  <header class="header-band">
    <div class="brand">
      <span class="brand-mark"></span>
      <span class="brand-name">MUSEUM<br>HAVBRINK</span>
    </div>
  </header>

  <div class="block block--title"></div>
  <div class="block block--date"></div>
  <div class="block block--side"></div>
  <div class="block block--lower"></div>
  <div class="block block--tagline"></div>

  <h1 class="title">
    <span class="title-line title-line--1">Whispers</span>
    <span class="title-line title-line--2">of</span>
    <span class="title-line title-line--3">Forgotten</span>
    <span class="title-line title-line--4">Ages</span>
  </h1>

  <p class="date">25 Sept 2020<br>6:00pm</p>
  <p class="tagline">an archaeological exhibition<br>about belief and superstition</p>
  <p class="details">Lorem ipsum dolor sit amet, consectetur adipiscing elit. Morbi ultricies molestie orci. Aenean purus mauris, sodales nec diam dignissim, porttitor laoreet enim. Aliquam id sollicitudin turpis. Vivamus aliquet elit sem, et ornare ex aliquam in. In cursus, felis non pretium molestie, tellus lacus facilisis metus, ut accumsan nisi nulla accumsan risus. Etiam id pharetra ante. Nunc sit amet ante id justo consequat tempor. Nullam pretium arcu eu hendrerit aliquam. Sed in purus eros.</p>
</main>
</body>
</html>
```